Zorvik App Graphics Design

Our application promotes location based self expression via pictures and text. The primary focus of the application is on the content posted and not on the person that posted it.

We want a very clean and fresh design that evokes positive energy. Our site is unique so our design should be as well. People will reveal thoughts on our site, so the design should convey a "revealing" feel. Our site is a place where people are comfortable to freely express themselves. Colors we have in mind are blue and green hues with earth tones for background.

Our project is to design ten screens for our Zorvik application at resolution of 1136-by-640 pixels:

Feed Screen
Camera Screen
Post Screen
Check In Screen
Approval Screen
Map Screen
Flag Screen
Feed Select Screen
Export Screen
Menu Screen

In the contest phase we will require only three screens to be submitted. The screens we require to be submitted are: Feed Screen; Map Screen and Camera Screen. The designer we select as the winner of the competition will then complete the project and deliver a total of the ten screens described above in the handover phase.

We have attached a document below with detailed specs of each screen, we ask for your innovation to bring these screens to life through your design.
Updates

We want to clarify one aspect regarding the VISOR: the visor needs to be transparent so that when the picture scrolls underneath it, you can still see the picture underneath the visor.

Hi Everyone,

We have noticed that some designers need clarification regarding the visor element in the feed screen.
I have attached two examples to our brief area called:
Visor Example 1 and Visor Example 2

Please note that these are not the style we are looking for but are a good example to the concept of a Transparent Visor above the feed stream. We are looking for you guys to come up with a Visor concept that is consistent with the style of the design you are submitting.

Thanks,

Bo

Target Market(s)

People 17-40 who want to share their thought about the world around them.

Industry/Entity Type

Flag

Font styles to use
Sans Serif
Other font styles liked:
• We like “Helvetica New” or “Avenir” but are flexible

Requirements
Must have
• Visor component should look innovative.

```html
<!DOCTYPE html>
<html lang="en">
<head>
<meta charset="utf-8">
<title>Zorvik App Screens</title>
<link rel="stylesheet" href="https://fonts.googleapis.com/css2?family=Roboto:wght@300;400;500;700&display=swap">
<style>
:root{
  --bg:#e6e9ea;
  --teal-deep:#17394a;
  --teal:#1f4d60;
  --teal-mid:#2b6a80;
  --teal-light:#4b93a8;
  --tab:#d3e0e5;
  --icon:#2a4f60;
  --white:#ffffff;
  --stat-bg:rgba(30,30,30,.72);
}
*{box-sizing:border-box;margin:0;padding:0}
html,body{width:1200px;height:1139px;overflow:hidden}
body{background:var(--bg);font-family:"Roboto",sans-serif;position:relative;color:var(--white)}
.screen{position:absolute;top:230px;width:364px;height:645px;overflow:hidden;background:var(--teal);box-shadow:0 6px 24px rgba(0,0,0,.18)}
.screen--feed{left:142px}
.screen--camera{left:670px}
.status-bar{height:24px;display:flex;align-items:center;justify-content:space-between;padding:0 8px;font-size:12.5px;white-space:nowrap;background:linear-gradient(90deg,var(--teal-deep),var(--teal-light) 50%,var(--teal-deep))}
.status-bar .carrier{display:flex;align-items:center;gap:4px}
.status-bar .battery{display:flex;align-items:center;gap:4px}
.battery-icon{width:26px;height:11px;border:1px solid var(--white);border-radius:2px;padding:1px}
.battery-icon span{display:block;width:100%;height:100%;background:var(--white)}
.nav-bar{height:50px;display:flex;align-items:center;justify-content:space-between;padding:0 12px;background:linear-gradient(90deg,#1e4e62,#3b8097 50%,#1e4e62)}
.nav-title{font-size:19px;font-weight:400;color:#0f2a36;white-space:nowrap}
.visor{height:66px;padding:14px 12px 0;font-size:14px;line-height:17px;font-weight:300;background:linear-gradient(180deg,rgba(33,92,112,.95),rgba(44,104,124,.9))}
.feed-photo{position:relative;height:342px;background:linear-gradient(135deg,#b9c7cc 0%,#e5eef2 35%,#7fb0d6 55%,#d8c4b3 75%,#eef2f3 100%)}
.overlay-btn{position:absolute;top:18px;width:50px;height:50px;background:rgba(35,35,35,.82);border-radius:3px;display:flex;align-items:center;justify-content:center}
.overlay-btn--flag{left:14px}
.overlay-btn--share{right:16px}
.stats{position:absolute;left:16px;top:286px;width:334px;height:46px;display:flex;background:var(--stat-bg)}
.stat{flex:1;text-align:center;padding-top:5px;border-right:1px solid rgba(255,255,255,.25)}
.stat:last-child{border-right:none}
.stat-value{font-size:19px;font-weight:700;line-height:20px}
.stat-label{font-size:11px;color:#b5bcbf;line-height:14px}
.vote-bar{height:68px;display:flex;background:linear-gradient(180deg,#1a4557,#21566a)}
.vote-btn{flex:1;display:flex;align-items:center;justify-content:center}
.vote-btn+.vote-btn{border-left:1px solid rgba(0,0,0,.25)}
.location{height:38px;display:flex;align-items:center;gap:6px;padding:0 22px;font-size:10px;font-weight:500;line-height:11px;white-space:nowrap;background:linear-gradient(90deg,#236178,#2f7a92)}
.tab-bar{height:57px;display:flex;align-items:center;justify-content:space-between;padding:0 18px;background:var(--tab)}
.camera-tools{height:50px;display:flex;align-items:center;justify-content:space-between;padding:0 14px;background:linear-gradient(90deg,#8c7255,#a58b6c 50%,#7d664e)}
.camera-tools .group{display:flex;gap:22px;align-items:center}
.camera-photo{height:388px;background:radial-gradient(ellipse at 55% 55%,#b9a48a 0%,#8f5a35 40%,#6b3a1f 75%,#4a2a18 100%)}
.filters{height:126px;padding:16px 0 0 14px;display:flex;gap:12px;background:linear-gradient(180deg,#3e8aa2,#1f5d74)}
.filter{width:80px;text-align:center;flex-shrink:0}
.filter-thumb{width:80px;height:80px;border:2px solid var(--white);background:linear-gradient(160deg,#c2703a,#8a4a24 60%,#d7a07a)}
.filter-thumb--mono{background:linear-gradient(160deg,#b8b8b8,#6c6c6c 60%,#d4d4d4)}
.filter-name{font-size:16px;margin-top:6px}
.tab-bar--camera{padding:0 22px}
</style>
</head>
<body>

<section class="screen screen--feed" aria-label="Feed screen">
  <div class="status-bar">
    <span class="carrier">●●●●● NOVA
      <svg width="14" height="11" viewBox="0 0 14 11" fill="none" stroke="#fff" stroke-width="1.4"><path d="M1 4a9 9 0 0 1 12 0M3.5 6.5a5.5 5.5 0 0 1 7 0"/><circle cx="7" cy="9" r="1" fill="#fff"/></svg>
    </span>
    <span>9:25 PM</span>
    <span class="battery">100% <span class="battery-icon"><span></span></span></span>
  </div>
  <header class="nav-bar">
    <svg width="26" height="22" viewBox="0 0 26 22" stroke="#0f2a36" stroke-width="2"><path d="M1 3h24M1 11h24M1 19h24"/></svg>
    <h1 class="nav-title">Zorvik Feeds</h1>
    <svg width="28" height="28" viewBox="0 0 28 28" fill="none" stroke="#0f2a36" stroke-width="2"><circle cx="12" cy="12" r="10"/><path d="M19 19l8 8"/></svg>
  </header>
  <p class="visor">In tortor sapien, egestas et enim vel, laoreet pulvinar felis. Quisque porttitor ornare euismod. Ut.</p>
  <div class="feed-photo" role="img" aria-label="Photo of hands pointing at a tablet showing business charts">
    <div class="overlay-btn overlay-btn--flag">
      <svg width="34" height="32" viewBox="0 0 34 32" fill="none" stroke="#fff" stroke-width="1.6"><path d="M3 2v29M3 4c8-4 14 4 28 0v16c-14 4-20-4-28 0"/></svg>
    </div>
    <div class="overlay-btn overlay-btn--share">
      <svg width="26" height="32" viewBox="0 0 26 32" fill="none" stroke="#fff" stroke-width="1.6"><path d="M13 2v19M7 8l6-6 6 6M8 13H2v17h22V13h-6"/></svg>
    </div>
    <div class="stats">
      <div class="stat"><div class="stat-value">15</div><div class="stat-label">Miles</div></div>
      <div class="stat"><div class="stat-value">485</div><div class="stat-label">Score</div></div>
      <div class="stat"><div class="stat-value">5</div><div class="stat-label">days ago</div></div>
    </div>
  </div>
  <div class="vote-bar">
    <div class="vote-btn"><svg width="26" height="30" viewBox="0 0 26 30" fill="none" stroke="#fff" stroke-width="1.6"><path d="M13 1L1 14h7v15h10V14h7z"/></svg></div>
    <div class="vote-btn"><svg width="26" height="30" viewBox="0 0 26 30" fill="none" stroke="#fff" stroke-width="1.6"><path d="M13 29L1 16h7V1h10v15h7z"/></svg></div>
  </div>
  <div class="location">
    <svg width="12" height="17" viewBox="0 0 12 17" fill="none" stroke="#fff" stroke-width="1.2"><path d="M6 16S1 9 1 6a5 5 0 0 1 10 0c0 3-5 10-5 10z"/><circle cx="6" cy="6" r="2"/></svg>
    <span>Grillhaus<br>48 Elm Avenue, Fairview, NY 10020</span>
  </div>
  <nav class="tab-bar">
    <svg width="38" height="32" viewBox="0 0 38 32" fill="none" stroke="var(--icon)" stroke-width="1.8"><rect x="1" y="7" width="36" height="24" rx="3"/><path d="M4 7V4h6v3M13 7l3-5h8l3 5"/><circle cx="19" cy="19" r="8"/><circle cx="19" cy="19" r="4.5"/></svg>
    <svg width="36" height="38" viewBox="0 0 36 38" fill="none" stroke="var(--icon)" stroke-width="1.8"><circle cx="18" cy="16" r="12"/><circle cx="18" cy="16" r="8"/><path d="M18 11l1.6 3.3 3.6.5-2.6 2.5.6 3.6-3.2-1.7-3.2 1.7.6-3.6-2.6-2.5 3.6-.5z" fill="var(--icon)"/><path d="M10 26l-4 10 5-2 3 4 3-8M26 26l4 10-5-2-3 4-3-8"/></svg>
  </nav>
</section>

<section class="screen screen--camera" aria-label="Camera screen">
  <div class="status-bar">
    <span class="carrier">●●●●● NOVA
      <svg width="14" height="11" viewBox="0 0 14 11" fill="none" stroke="#fff" stroke-width="1.4"><path d="M1 4a9 9 0 0 1 12 0M3.5 6.5a5.5 5.5 0 0 1 7 0"/><circle cx="7" cy="9" r="1" fill="#fff"/></svg>
    </span>
    <span>9:25 PM</span>
    <span class="battery">100% <span class="battery-icon"><span></span></span></span>
  </div>
  <div class="camera-tools">
    <div class="group">
      <svg width="20" height="28" viewBox="0 0 20 28" fill="none" stroke="#fff" stroke-width="1.4"><path d="M13 1L3 16h7l-4 11 11-16h-7z"/></svg>
      <svg width="32" height="28" viewBox="0 0 32 28" fill="none" stroke="#fff" stroke-width="1.6"><path d="M27 16A12 12 0 1 1 24 6M24 1v6h6"/></svg>
    </div>
    <div class="group">
      <svg width="30" height="30" viewBox="0 0 30 30" fill="none" stroke="#fff" stroke-width="1.6"><path d="M1 9V1h8M21 1h8v8M29 21v8h-8M9 29H1v-8"/><circle cx="15" cy="15" r="2"/></svg>
      <svg width="30" height="30" viewBox="0 0 30 30" fill="none" stroke="#fff" stroke-width="1.6"><circle cx="15" cy="15" r="13.5"/><path d="M10 10l10 10M20 10L10 20"/></svg>
    </div>
  </div>
  <div class="camera-photo" role="img" aria-label="Photo of brass scales of justice on a wooden desk"></div>
  <div class="filters">
    <div class="filter"><div class="filter-thumb" role="img" aria-label="Vivid filter preview"></div><div class="filter-name">Vivid</div></div>
    <div class="filter"><div class="filter-thumb filter-thumb--mono" role="img" aria-label="Mono filter preview"></div><div class="filter-name">Mono</div></div>
    <div class="filter"><div class="filter-thumb" role="img" aria-label="Instant filter preview"></div><div class="filter-name">Instant</div></div>
    <div class="filter"><div class="filter-thumb" role="img" aria-label="Pro filter preview"></div><div class="filter-name">Pro</div></div>
  </div>
  <nav class="tab-bar tab-bar--camera">
    <svg width="34" height="28" viewBox="0 0 34 28" fill="none" stroke="var(--icon)" stroke-width="1.6"><rect x="1" y="6" width="32" height="21" rx="3"/><path d="M4 6V3h5v3"/><circle cx="19" cy="16" r="7"/><circle cx="19" cy="16" r="3.5"/></svg>
    <svg width="32" height="32" viewBox="0 0 32 32" fill="none" stroke="var(--icon)" stroke-width="1.6"><circle cx="16" cy="16" r="7"/><path d="M16 1v5M16 26v5M1 16h5M26 16h5M5.4 5.4l3.5 3.5M23.1 23.1l3.5 3.5M5.4 26.6l3.5-3.5M23.1 8.9l3.5-3.5"/></svg>
    <svg width="34" height="28" viewBox="0 0 34 28" fill="none" stroke="var(--icon)" stroke-width="1.6"><rect x="1" y="6" width="32" height="21" rx="3"/><path d="M11 6l3-5h6l3 5"/><circle cx="17" cy="16" r="7"/><circle cx="17" cy="16" r="3.5"/></svg>
    <svg width="32" height="32" viewBox="0 0 32 32" fill="none" stroke="var(--icon)" stroke-width="1.6"><path d="M7 1v24h24M1 7h24v24M1 31L31 1"/></svg>
    <svg width="34" height="28" viewBox="0 0 34 28" fill="none" stroke="var(--icon)" stroke-width="1.8"><rect x="1" y="1" width="32" height="26"/><path d="M4 24l9-10 6 6 4-3 8 7z" fill="var(--icon)"/><circle cx="24" cy="8" r="3"/></svg>
  </nav>
</section>

</body>
</html>
```